Book Cover Design

Design with title UNWAVERING
Subtitle: Ways to Kindle the Spark of Resolve
Author Name: Carla Jean Morrow
Put DAILY MERIDIAN BESTSELLER at top
Shimmer design, see inspirational images attached

```html
<!DOCTYPE html>
<html lang="en">
<head>
<meta charset="UTF-8">
<title>Unwavering — Book Cover</title>
<link rel="stylesheet" href="https://fonts.googleapis.com/css2?family=Days+One&family=Fredoka:wght@400;500&display=swap">
<style>
  :root {
    --stage: #ffffff;
    --parchment-light: #fbf1d6;
    --parchment-mid: #f6dfae;
    --parchment-warm: #efcb8c;
    --glow: #fffaf0;
    --ink: #2a1318;
    --ink-shadow: rgba(90, 70, 60, 0.45);
    --rock-top: rgba(142, 45, 21, 0);
    --rock-glow: rgba(142, 45, 21, 0.75);
    --rock-mid: #5c1c12;
    --rock-base: #2a1412;
    --paper-text: #ffffff;
  }
  * { margin: 0; padding: 0; box-sizing: border-box; }
  html, body {
    width: 1200px;
    height: 1000px;
    overflow: hidden;
    background: var(--stage);
  }
  .canvas {
    position: relative;
    width: 1200px;
    height: 1000px;
  }
  .book-cover {
    position: absolute;
    left: 263px;
    top: 24px;
    width: 673px;
    height: 953px;
    overflow: hidden;
    background:
      radial-gradient(ellipse 55% 32% at 40% 42%, var(--glow) 0%, rgba(255,250,240,0) 70%),
      radial-gradient(ellipse 70% 40% at 80% 20%, var(--parchment-light) 0%, rgba(251,241,214,0) 70%),
      linear-gradient(180deg, var(--parchment-mid) 0%, var(--parchment-light) 35%, var(--parchment-mid) 60%, var(--parchment-warm) 100%);
  }
  .bestseller-tag {
    position: absolute;
    top: 38px;
    left: 0;
    width: 100%;
    text-align: center;
    font-family: "Days One", sans-serif;
    font-size: 27px;
    letter-spacing: 0.5px;
    color: var(--ink);
  }
  .author-name {
    position: absolute;
    top: 210px;
    left: 0;
    width: 100%;
    text-align: center;
    font-family: "Fredoka", sans-serif;
    font-weight: 500;
    font-size: 50px;
    color: var(--ink);
    text-shadow: 2px 2px 0 rgba(200, 140, 120, 0.5);
  }
  .title-rule {
    position: absolute;
    top: 340px;
    left: 228px;
    width: 194px;
    height: 4px;
    background: var(--ink);
  }
  .book-title {
    position: absolute;
    top: 404px;
    left: 0;
    width: 100%;
    text-align: center;
    font-family: "Days One", sans-serif;
    font-size: 60px;
    letter-spacing: 0.5px;
    color: var(--ink);
    text-shadow: 5px 6px 0 var(--ink-shadow);
  }
  .summit-photo {
    position: absolute;
    left: 0;
    top: 520px;
    width: 673px;
    height: 433px;
    background: linear-gradient(180deg, var(--rock-top) 0%, var(--rock-glow) 38%, var(--rock-mid) 62%, var(--rock-base) 100%);
  }
  .book-subtitle {
    position: absolute;
    top: 800px;
    left: 0;
    width: 100%;
    text-align: center;
    font-family: "Fredoka", sans-serif;
    font-weight: 400;
    font-size: 27px;
    line-height: 37px;
    color: var(--paper-text);
  }
</style>
</head>
<body>
<main class="canvas">
  <article class="book-cover">
    <p class="bestseller-tag">DAILY MERIDIAN BESTSELLER</p>
    <p class="author-name">Carla Jean Morrow</p>
    <div class="title-rule"></div>
    <h1 class="book-title">UNWAVERING</h1>
    <div class="summit-photo" role="img" aria-label="Photograph of a person with raised arms standing on a rocky mountain summit in warm sunrise light"></div>
    <p class="book-subtitle">Ways to Kindle the Spark<br>of Resolve</p>
  </article>
</main>
</body>
</html>
```